演奏会のメイン曲は、ベネディクト・ハウエル作曲「ラ・フォンテ・ヴェルデ」です。
演奏会全体としては、”希望の光”をイメージしています。
依然コロナ禍にありますが、音楽が”希望の光”になれば…
また、西海沿岸大洪水から10年で、復興支援のために作られた曲も演奏を予定しています。
・団体名
・演奏会名:ハーモニーフェスタ2021
・指揮者名:柳沼俊哉
・場所
・日時:2021年12月12日(日)
・曲目:ラ・フォンテ・ヴェルデ、星は今も瞬く、マルコの幻想の朝、夢にさそわれて…他
・問い合わせ先:担当/水野 090-2716-4098、https://sakuragi-brass.hoshizora-web.com/
など
※場所、チケット情報などは、添付画像と変化なしです。ご覧いただければと思います。
A4
片面
過去のチラシデータを添付いたしますので、ご参照ください。
チラシのデザインが決まれば、チラシのデザインを基に、チケット・ポスター・パンフレットの表紙も追加(1万程度)で作成していただきたいと考えております。
よろしくお願いします。
たくさんのご提案、ありがとうございます。
どれも素敵なデザインで、迷ってしまうという嬉しい悩みです。
わたし個人では決められないため、団体内で相談しようと思います。
相談できる日がお盆明けになる関係で、締め切りを延長しました。
引き続きよろしくお願いいたします。

クリスマスが近い時期の演奏会、という雰囲気に心惹かれました。
また、おしゃれさや見やすさ、演奏会全体の「希望に満ちたイメージ」との相性も含め、こちらのデザインに決めさせていただきました。

すてきなデザインをたくさんご応募いただき、本当にありがとうございました。
他のデザインにも、とても心惹かれました。
またよろしくお願いいたします。

```html
<!DOCTYPE html>
<html lang="ja">
<head>
<meta charset="utf-8">
<title>桜木市民吹奏楽団 ハーモニーフェスタ2021</title>
<link rel="stylesheet" href="https://fonts.googleapis.com/css2?family=Noto+Serif+JP:wght@400;600;700;900&display=swap">
<style>
  :root {
    --ink: #050403;
    --white: #ffffff;
    --soft: #e9e4da;
    --gold-light: #fff2c4;
    --gold: #e3b65a;
    --gold-deep: #a8741f;
  }
  * { margin: 0; padding: 0; box-sizing: border-box; }
  html, body { width: 846px; height: 1200px; overflow: hidden; background: var(--ink); }
  .flyer {
    position: relative;
    width: 846px;
    height: 1200px;
    overflow: hidden;
    font-family: "Noto Serif JP", serif;
    color: var(--white);
    background:
      radial-gradient(ellipse 360px 260px at 430px -20px, rgba(255, 240, 200, 0.95), rgba(240, 180, 80, 0.45) 45%, transparent 80%),
      radial-gradient(ellipse 620px 700px at 430px 80px, rgba(200, 140, 50, 0.35), transparent 70%),
      radial-gradient(ellipse 500px 300px at 420px 1200px, rgba(180, 120, 40, 0.25), transparent 75%),
      var(--ink);
  }
  .light-rays {
    position: absolute;
    inset: 0;
    background: conic-gradient(from 150deg at 430px -40px,
      transparent 0deg, rgba(255, 220, 150, 0.18) 6deg, transparent 12deg,
      rgba(255, 220, 150, 0.12) 20deg, transparent 26deg,
      rgba(255, 230, 170, 0.2) 32deg, transparent 38deg,
      rgba(255, 220, 150, 0.14) 46deg, transparent 52deg,
      rgba(255, 220, 150, 0.16) 58deg, transparent 64deg);
  }
  .gold {
    background: linear-gradient(180deg, var(--gold-light), var(--gold) 45%, var(--gold-deep));
    -webkit-background-clip: text;
    background-clip: text;
    color: transparent;
  }
  .vertical { writing-mode: vertical-rl; text-orientation: upright; }

  .group-name {
    position: absolute;
    left: 748px; top: 22px;
    font-size: 62px; font-weight: 700;
    letter-spacing: 2px;
    line-height: 1;
  }
  .concert-title {
    position: absolute;
    left: 18px; top: 150px;
    font-size: 86px; font-weight: 700;
    line-height: 1;
    letter-spacing: 2px;
  }
  .concert-year {
    position: absolute;
    left: 14px; top: 1072px;
    font-size: 118px; font-weight: 700;
    line-height: 1;
    letter-spacing: -2px;
  }
  .catch {
    position: absolute;
    font-size: 36px; font-weight: 600;
    letter-spacing: 10px;
    line-height: 1;
  }
  .catch-music { left: 420px; top: 110px; }
  .catch-hope { left: 350px; top: 180px; }

  .date {
    position: absolute;
    left: 262px; top: 492px;
    font-size: 50px; font-weight: 700;
    line-height: 1;
    white-space: nowrap;
  }
  .date .week {
    display: inline-block;
    font-size: 28px;
    background: var(--white); color: var(--ink);
    padding: 2px 4px; border-radius: 3px;
    vertical-align: 8px;
  }
  .time {
    position: absolute; left: 268px; top: 556px;
    font-size: 15px; letter-spacing: 1px; color: var(--soft);
  }
  .venue {
    position: absolute; left: 268px; top: 582px;
    font-size: 24px; font-weight: 600;
  }
  .conductor {
    position: absolute; left: 392px; top: 638px;
    font-size: 32px; font-weight: 700; letter-spacing: 4px;
  }
  .program {
    position: absolute; left: 392px; top: 700px;
    font-size: 22px; font-weight: 600; line-height: 1.55;
    list-style: none;
  }
  .program .label { font-size: 16px; font-weight: 400; color: var(--soft); }

  .ticket {
    position: absolute; left: 130px; top: 950px;
    width: 480px;
    font-size: 11px; line-height: 1.6; color: var(--soft);
  }
  .ticket .price { font-size: 32px; font-weight: 700; color: var(--white); line-height: 1.1; }
  .ticket .row { display: flex; gap: 10px; align-items: baseline; }

  .access-note {
    position: absolute; left: 640px; top: 690px;
    width: 180px;
    font-size: 10px; line-height: 1.5; color: var(--soft);
  }
  .map {
    position: absolute; left: 628px; top: 790px;
    width: 196px; height: 140px;
    background: var(--white);
    display: flex; align-items: center; justify-content: center;
    color: var(--ink); font-size: 20px;
  }
  .footer-note {
    position: absolute; left: 330px; right: 22px; top: 1132px;
    font-size: 10px; line-height: 1.6; color: var(--soft); text-align: right;
  }
</style>
</head>
<body>
  <main class="flyer">
    <div class="light-rays" aria-hidden="true"></div>

    <h1 class="group-name vertical">桜木市民吹奏楽団</h1>
    <h2 class="concert-title vertical gold">ハーモニーフェスタ</h2>
    <div class="concert-year gold">2021</div>

    <p class="catch catch-music vertical gold">音楽による</p>
    <p class="catch catch-hope vertical gold">希望の光</p>

    <p class="date">2021年12月12日<span class="week">日</span></p>
    <p class="time">開場 00:00 / 開演 00:00（終演予定 00:00）</p>
    <p class="venue">桜木市文化会館　大ホール</p>

    <p class="conductor">指揮　柳沼俊哉</p>
    <ul class="program">
      <li class="label">曲目</li>
      <li>ラ・フォンテ・ヴェルデ</li>
      <li>星は今も瞬く</li>
      <li>マルコの幻想の朝</li>
      <li>夢にさそわれて…他</li>
    </ul>

    <p class="access-note">アクセス：桜木駅より徒歩10分<br>駐車場に限りがございます</p>
    <div class="map" role="img" aria-label="桜木市文化会館までの地図">地図</div>

    <section class="ticket">
      <div class="row"><span>前売券・当日券／一般</span><span class="price">¥500</span></div>
      <p>※未就学児の入場はご遠慮ください。全席自由です。</p>
      <p>チケット取扱所：桜木市文化会館・市内楽器店</p>
      <p>問い合わせ：担当／水野　090-2716-4098</p>
      <p>https://sakuragi-brass.hoshizora-web.com/</p>
    </section>

    <p class="footer-note">本公演は西海沿岸大洪水の復興支援を目的としています。<br>主催：桜木市民吹奏楽団　後援：桜木市・桜木市教育委員会</p>
  </main>
</body>
</html>
```